依頼詳細
新築工事現場にかける会社のイメージシートのデザインをお願い致します。
会社のイメージを高め、会社名と事業内容を知ってもらうことが作成の目的です。

「時代の一歩先を行くハイクオリティでスタイリッシュな上質な空間を創造し、心にゆ
とりを与え、人生を豊かにする住まいを提供する」

会社のミッションは上記となるので
「おしゃれな家を創っている、ハウスビルダー」と
シートを見た方にイメージしてもらえるデザインを希望しています。

写真や文字で細かく表現するよりも、パッと見た時に目をひく、インパクトがあるものが良いと考えています。
家全体を覆うグレイのビニールシートの上に貼る感じなので、そちらも踏まえたカラーリング、デザインをお願いできれば幸いです。
記載項目
ロゴマーク/会社名/キャッチコピー 横1800×縦3600
希望イメージ
シンプル 複雑
単色 カラフル
暗い 明るい
日常 高級
遊び心 厳粛
未来的 伝統的
女性的 男性的
希望する色
黄・オレンジ系、緑系
納品ファイル
• 高解像度JPG (.jpg)
• イラストレーター形式 (.ai)
• フォトショップ形式 (.psd)
• PNG形式 (.png)
補足説明
遠くから見たり、車で走行中に目に入る感じなので、たくさんの文字が入るよりも、できるだけシンプルなものがいいと考えています。
以下の項目は必須で入れていただきたい項目です。

・会社名【株式会社オリベテック】
・検索窓
・ロゴ
・URL【http://olivetec-home.co.jp

宜しくお願い致します。
■ 選んだ理由

シンプルで高級感のあるデザインが気にいりました。

■ 提案者全員のお礼・コメント

皆様、たくさんのご提案ありがとうございました。
素晴らしいご提案がたくさんあり、選出にはとても悩みました。
今後もTadplexさんを活用していくことがあると思いますので、その際はまたお力添えを頂ければ幸いです。

```html
<!DOCTYPE html>
<html lang="ja">
<head>
<meta charset="utf-8">
<title>株式会社オリベテック 工事現場シート</title>
<link rel="stylesheet" href="https://fonts.googleapis.com/css2?family=Noto+Sans+JP:wght@400;500;900&display=swap">
<style>
  :root{
    --backdrop:#e4e5e7;
    --orange:#f39322;
    --cream:#fff4e4;
    --ink:#1e1a16;
    --divider:#6b6b6b;
    --white:#ffffff;
    --brand-green:#7fa33a;
    --text-gray:#555555;
    --field-border:#9a9a9a;
    --button-gray:#8a8a8a;
  }
  html,body{margin:0;padding:0;}
  body{
    width:848px;height:1200px;overflow:hidden;
    background:var(--backdrop);
    font-family:"Noto Sans JP",sans-serif;
    position:relative;
  }
  .sheet{
    position:absolute;left:160px;top:86px;
    width:528px;height:1032px;
    background:var(--white);
    box-shadow:0 2px 8px rgba(0,0,0,.15);
    overflow:hidden;
  }
  .hero{
    position:absolute;left:0;top:0;width:100%;height:720px;
    background:var(--orange);
  }
  .catchcopy{
    position:absolute;left:112px;top:42px;margin:0;
    font-weight:900;font-size:62px;line-height:92px;
    color:var(--ink);letter-spacing:2px;
  }
  .catchcopy span{display:block;}
  .hero-illustration{
    position:absolute;left:14px;top:336px;width:500px;height:336px;
    border-radius:48px;
    background:radial-gradient(ellipse at 50% 50%,var(--cream) 0%,#fbd9a8 40%,var(--orange) 78%);
  }
  .divider{
    position:absolute;left:0;top:720px;width:100%;height:12px;
    background:var(--divider);
  }
  .brand{
    position:absolute;left:0;top:790px;width:100%;
    display:flex;justify-content:center;align-items:center;gap:18px;
  }
  .brand-mark{width:44px;height:44px;background:var(--brand-green);}
  .brand-name{
    font-weight:500;font-size:44px;line-height:56px;color:var(--text-gray);letter-spacing:2px;
  }
  .search{
    position:absolute;left:80px;top:902px;
    display:flex;gap:8px;align-items:center;
  }
  .search-field{
    width:236px;height:38px;box-sizing:border-box;
    border:2px solid var(--field-border);background:var(--white);
    font-size:20px;line-height:34px;padding-left:8px;color:var(--ink);
  }
  .search-button{
    width:76px;height:38px;background:var(--button-gray);color:var(--white);
    font-size:20px;line-height:38px;text-align:center;border-radius:3px;
  }
  .url{
    position:absolute;left:0;top:968px;margin:0;width:100%;text-align:center;
    font-size:26px;line-height:36px;color:var(--text-gray);letter-spacing:.5px;
  }
</style>
</head>
<body>
  <main class="sheet">
    <section class="hero">
      <h1 class="catchcopy"><span>人生を</span><span>豊かにする</span><span>住まい。</span></h1>
      <div class="hero-illustration" role="img" aria-label="白い線で描かれた、リボンでつながる二つのハートと小さなハートのイラスト"></div>
    </section>
    <div class="divider"></div>
    <div class="brand">
      <div class="brand-mark"></div>
      <div class="brand-name">オリベテック</div>
    </div>
    <div class="search">
      <div class="search-field">オリベテック</div>
      <div class="search-button">検索</div>
    </div>
    <p class="url">http://olivetec-home.co.jp</p>
  </main>
</body>
</html>
```